Website

Project to include our logo, (files attached - logo only to be included with the company name K&T Chemicals, Inc.). Visit the website to gather additional information. www.kandtchemicals-site.example.
Emphasis should be more on the trucking, (tanker trucks), and blending capabilities. See pictures on website.
Please incorporate the logo colors into the website design; particularly the darker blue and red.
Updates
I have updated the brief on this project. :)
I have just updated the brief.
The deadline is Sunday.
Please submit your final designs.
Thanks :)
Today is the last day to submit your designs.
Industry/Entity Type
It Company
Requirements
Must have
- Tank Truck picture/s and Rail Car pictures.
See this website for tank truck and rail picture (also shown below): http://freightlens.example/562/u-s-power-surge-respite-and-a-tally-says-vbt-ostrand-and-kellaway/

```html
<!DOCTYPE html>
<html lang="en">
<head>
<meta charset="utf-8">
<title>K&amp;T Chemicals, Inc.</title>
<link rel="stylesheet" href="https://fonts.googleapis.com/css2?family=PT+Sans:wght@400;700&display=swap">
<style>
:root{
  --white:#ffffff;
  --page:#e6e6e6;
  --ink:#444448;
  --muted:#7a7a7a;
  --navy:#2e2f86;
  --violet:#5f5fa8;
  --violet-light:#7474b8;
  --violet-dark:#4d4d96;
  --cyan:#2aa8cc;
  --tile:#2f2f2f;
  --sky-top:#5d86c9;
  --sky-bottom:#a9bfdc;
  --night-top:#0c0f1a;
  --night-bottom:#5a4b3a;
}
*{margin:0;padding:0;box-sizing:border-box}
html,body{width:1200px;height:913px;overflow:hidden;background:var(--white)}
body{font-family:"PT Sans",sans-serif;color:var(--ink)}
.canvas{position:relative;width:1200px;height:913px;overflow:hidden}

/* sidebar */
.sidebar{position:absolute;left:0;top:0;width:270px;height:913px;background:var(--white)}
.sidebar-shapes{position:absolute;left:0;top:0}
.brand{position:absolute;left:20px;top:58px;width:210px}
.brand-row{display:flex;align-items:center;gap:8px}
.brand-dot{width:34px;height:34px;border-radius:50%;background:var(--navy);flex:none}
.brand-name{font-size:25px;font-weight:700;color:var(--navy);line-height:1.05}
.brand-meta{margin-top:8px;text-align:right;font-size:6.5px;line-height:9px;color:var(--navy)}
.main-nav{position:absolute;left:20px;top:264px;list-style:none}
.main-nav li{font-size:14px;line-height:23px;color:var(--white);text-transform:uppercase}
.nav-marker{position:absolute;left:0;top:266px;width:0;height:0;border-top:7px solid transparent;border-bottom:7px solid transparent;border-left:7px solid var(--white)}
.side-heading{position:absolute;left:22px;font-size:11px;color:var(--white)}
.updates-title{top:387px}
.updates-text{position:absolute;left:20px;top:414px;width:225px;font-size:8.5px;line-height:14px;color:var(--white)}
.updates-text .hl{background:var(--white);color:var(--navy);text-decoration:underline}
.social-title{top:545px}
.social{position:absolute;left:21px;top:573px;display:flex;gap:3px}
.social-tile{width:26px;height:24px;background:var(--tile);display:flex;align-items:center;justify-content:center}
.copyright{position:absolute;left:22px;top:843px;font-size:8.5px;color:var(--muted)}

/* main column */
.content{position:absolute;left:270px;top:0;width:524px;height:913px;background:var(--page);overflow:hidden}
.content-shapes{position:absolute;left:0;top:0}
.topline{position:absolute;left:20px;top:9px;font-size:11px;color:var(--muted)}
.breadcrumb{position:absolute;left:21px;top:87px;font-size:8px;color:var(--ink)}
.tagline{position:absolute;left:20px;font-size:15px;color:var(--cyan);font-weight:400}
.tagline-1{top:138px}
.tagline-2{top:173px}
.copy{position:absolute;left:20px;top:230px;width:480px}
.copy p{font-size:10.5px;line-height:18px;color:var(--ink);margin-bottom:31px}
.copy .mark{color:var(--navy)}
.enquiries{position:absolute;left:21px;top:730px;width:474px}
.enquiries h2{font-size:8.5px;font-weight:700;color:var(--ink);padding-bottom:6px;border-bottom:1px solid #c9c9c9}
.enquiries .contact{font-size:8.5px;color:var(--ink);margin-top:16px}
.enquiries .contact + .contact{margin-top:12px}
.enquiries .sister{font-size:8.5px;color:var(--ink);margin-top:22px}
.enquiries .sister b{font-weight:700}

/* imagery column */
.photo{position:absolute;left:794px;width:406px}
.photo-plant{top:0;height:571px;background:linear-gradient(180deg,var(--sky-top) 0%,var(--sky-bottom) 70%,#8e96a3 100%)}
.photo-night{top:597px;height:316px;background:linear-gradient(180deg,var(--night-top) 0%,#1e1b22 40%,var(--night-bottom) 100%)}
</style>
</head>
<body>
<div class="canvas">

  <aside class="sidebar">
    <svg class="sidebar-shapes" width="270" height="913" viewBox="0 0 270 913" aria-hidden="true">
      <polygon points="0,185 270,293 270,668 0,842" fill="var(--violet)"/>
      <polygon points="0,478 240,590 0,700" fill="var(--violet-dark)" opacity=".55"/>
      <polygon points="0,700 270,596 270,622 0,740" fill="var(--violet-light)" opacity=".7"/>
      <polygon points="0,760 270,640 270,668 0,800" fill="var(--violet-light)" opacity=".6"/>
      <polygon points="0,800 270,668 270,686 0,842" fill="var(--violet-dark)"/>
    </svg>

    <div class="brand">
      <div class="brand-row">
        <span class="brand-dot"></span>
        <span class="brand-name">K&amp;T Chemicals, Inc.</span>
      </div>
      <div class="brand-meta">
        48 Mill Row • P.O. Box 310 • Harlow Springs, Georgia 30999<br>
        800.555.0142 • 770.555.0187 • Fax 770.555.0193<br>
        www.kandtchemicals-site.example
      </div>
    </div>

    <span class="nav-marker"></span>
    <ul class="main-nav">
      <li>Home</li>
      <li>Products</li>
      <li>Contact Us</li>
    </ul>

    <h3 class="side-heading updates-title">Latest Updates</h3>
    <p class="updates-text">Lorem ipsum dolor sit amet, <span class="hl">consectetur adipisicing</span> elit, sed do eiusmod tempor incididunt ut labore et dolore magna aliqua.</p>

    <h3 class="side-heading social-title">Social Links</h3>
    <div class="social">
      <span class="social-tile" aria-label="Social link"></span>
      <span class="social-tile" aria-label="Social link"></span>
      <span class="social-tile" aria-label="Social link"></span>
      <span class="social-tile" aria-label="More links">
        <svg width="12" height="12" viewBox="0 0 12 12" aria-hidden="true"><rect x="4.5" y="0" width="3" height="12" fill="#fff"/><rect x="0" y="4.5" width="12" height="3" fill="#fff"/></svg>
      </span>
    </div>

    <p class="copyright">© 2014 K &amp; T Chemicals, INC. All rights reserved.</p>
  </aside>

  <main class="content">
    <svg class="content-shapes" width="524" height="913" viewBox="0 0 524 913" aria-hidden="true">
      <polygon points="0,0 0,120 190,100 250,0" fill="#fff" opacity=".35"/>
      <polygon points="0,0 310,420 0,560" fill="#fff" opacity=".18"/>
      <polygon points="0,595 300,712 0,820" fill="#fff" opacity=".45"/>
      <polygon points="0,300 180,0 0,0" fill="#fff" opacity=".2"/>
    </svg>

    <p class="topline">K &amp; T Chemicals, Inc. Phone: (800) 555-0142</p>
    <p class="breadcrumb">Lorem ipsum &nbsp;&gt;&nbsp; Lorem ipsum</p>

    <h1 class="tagline tagline-1">Manufacturers and Distributors of Industrial Chemicals</h1>
    <h2 class="tagline tagline-2">Custom Blending of Dry &amp; Liquid Products</h2>

    <div class="copy">
      <p><span class="mark">K&amp;T</span> Services was a division of the Brandt and Ollery Company and was established in 1979 with the initial intent of recovering the Phosphate value of co-product 35% Phosphoric Acid from aluminum anodizing. Trisodium Phosphate was derived from this process by a unique patented procedure.</p>
      <p>The assets of K&amp;T Services were purchased in September 1993 by Martin Ashgrove and incorporated thereafter as <span class="mark">K&amp;T</span> Chemicals, Inc.</p>
      <p><span class="mark">K &amp; T</span> Chemicals blends and distributes dry and wet products. These items are packaged in bags, drums, totes and tank trucks.</p>
      <p>Due to our ability to blend and hold inventory and our dedicated truck fleet, we are able to respond immediately to new orders as we thrive in a “just in time” delivery situation.</p>
      <p>We are located near metro Riverton in Harlow Springs, Georgia. Our plant capabilities, rail line access, 400,000 gallon tank farm and 65,000 square foot warehouse, enables <span class="mark">K &amp; T</span> to be a leader in it’s unique niche.</p>
    </div>

    <section class="enquiries">
      <h2>For More Enquiries:</h2>
      <p class="contact">Martin Ashgrove / General Manager M.Ashgrove@kandtchemicals-site.example</p>
      <p class="contact">Lena Corrigan / Sales Manager L.Corrigan@mailbox.example</p>
      <p class="contact">Owen Pritchard / Operations Manager O.Pritchard@kandtchemicals-site.example</p>
      <p class="sister">If you are in need of gallon or quart case products, please visit our sister company: <b>QRSChemical.example</b></p>
    </section>
  </main>

  <div class="photo photo-plant" role="img" aria-label="Photo of a steel chemical processing plant with towers and pipework under a blue sky"></div>
  <div class="photo photo-night" role="img" aria-label="Photo of an industrial refinery lit up at night"></div>

</div>
</body>
</html>
```